Car Wash - Total Redesign For New Owner - WIX or WordPress

Needs to be coded for WIX but will accept WordPress for outstanding designs.
This company has just been purchased and we now have a fresh logo to start off a totally new redesign of the web presence.
Sites I like:
https://www.vornelink.com.au/
https://www.qarrowtech.com/au-en/
http://plinthova.com/#homepage1
https://www.brelstondw.com.au/
What we sell can be found at the old website: www.glimmabaywa.com.au
The package names have changed. Current package names uploaded "Price List.jpg"
I like the product descriptions at https://www.brelstondw.com.au/
The new logo and prices have been uploaded. If it isn't on the price list, please don't carry it over from the old site.
The picture on the home page background should not be a car dashboard or an actual car wash. The image and the website will suggest luxury and having extra time to do things because you are not washing a car. Maybe you now have time to drive along a beautiful winding road by the sea? Or surprise me with an abstract background of colour or water droplets or something entirely different!
Please do something stunning that catches the eye. It must NOT look like I made it myself using a web building wizard.
Look at the websites I like - They will start you off.
Thanks and have fun!
Target Market(s)
We're selling a service that is geared for both male and females with higher incomes. They are 20-50 and usually have a car new car only a year or two old. They like nice ordered surroundings and a spotless car but don't have the time to clean it themselves.
Industry/Entity Type
Automotive
Requirements
Must have
- The theme is clean, easy to navigate but has a stunning visual impact.
- Online Bookings, Online Payment, Email Us
- Must look attractive and load quickly on mobile devices
- If you want a general idea of background image I think would be different for the home page, look at something similar to
- www.pixtorvale.com/pic-81264057/stock-photo-photo-of-water-splash-isolated-on-black.html?src=72kTzQmLpW8vHcnYdRsEBA-1-47 would do it.
- I'm not saying you have to use this picture. Just be aware I want something different. I want to grab people's attention with something a bit different.
Nice to have
- Very clean on the home page. Possibly a background of moving water or water drops. Close-ups of: clean car interiors; polished and glossy external surfaces. The home page does not have to have a picture but can be an abstract design, close up of an object or material (water or soap). If there is a picture on the home page, the theme must be about relaxation, luxury, beauty.
Should not have
- No before/after pictures on the home page.
- On the home page, do not use a picture where the specific model of car is obvious. It makes the website look too much like a car dealership!

```html
<!DOCTYPE html>
<html lang="en">
<head>
<meta charset="utf-8">
<title>glimmabay wa – Automotive Detailing</title>
<link href="https://fonts.googleapis.com/css2?family=Exo+2:wght@600;700;800&family=Lato:wght@400;700&display=swap" rel="stylesheet">
<style>
:root{
  --ink:#111;
  --black:#050505;
  --accent:#2a9bd1;
  --accent-dark:#1a6f9e;
  --panel:#eeeeee;
  --side:#e2e2e2;
  --rule:#cfcfcf;
  --teal:#3b9cc8;
  --text:#222;
  --muted:#555;
  --white:#fff;
}
*{box-sizing:border-box;margin:0;padding:0}
html,body{width:686px;height:1200px;overflow:hidden}
body{position:relative;font-family:"Lato",Arial,sans-serif;color:var(--text);background:var(--white)}
.abs{position:absolute}
.heading{font-family:"Exo 2","Arial Black",sans-serif;font-weight:700}

/* hero */
.hero{position:absolute;left:0;top:0;width:686px;height:378px;background:var(--black);overflow:hidden}
.hero-photo{position:absolute;inset:0;background:radial-gradient(ellipse at 28% 40%,#f4f4f4 0%,#cfcfcf 30%,#8a8a8a 52%,#2a2a2a 72%,#050505 88%)}
.brand{position:absolute;left:76px;top:24px;display:flex;align-items:center;gap:7px;color:var(--white);font-family:"Exo 2",sans-serif;font-weight:700;font-size:19px;letter-spacing:.3px}
.brand-dot{width:14px;height:14px;border-radius:50%;background:var(--accent)}
.info{position:absolute;top:7px;display:flex;align-items:center;gap:5px;color:var(--white);font-size:6.4px;line-height:8px}
.info svg{width:14px;height:14px;flex:none}
.info b{font-size:7.2px}
.nav-top{position:absolute;left:282px;top:34px;width:328px;border-top:1px solid #333}
.main-nav{position:absolute;right:76px;top:43px;display:flex;gap:17px;font-size:8.2px;font-weight:700;color:var(--white)}
.main-nav .on{color:var(--accent)}
.hero-title{position:absolute;right:77px;top:128px;text-align:right;font-family:"Exo 2",sans-serif;font-weight:800;font-size:22px;line-height:31px;color:var(--white);text-shadow:0 0 8px rgba(255,255,255,.45);letter-spacing:.3px}
.arrow-box{position:absolute;top:178px;width:17px;height:20px;background:#666;display:flex;align-items:center;justify-content:center}
.arrow-box svg{width:8px;height:10px}

/* welcome */
.welcome-title{position:absolute;top:401px;left:0;width:686px;text-align:center;font-size:19px;color:var(--ink)}
.divider{position:absolute;top:434px;left:243px;width:200px;height:1px;background:var(--rule)}
.divider i{position:absolute;left:94px;top:-3px;width:12px;height:6px;border-radius:50%;background:var(--white);border:1.5px solid #999}
.welcome-copy{position:absolute;top:451px;left:76px;width:534px;text-align:center;font-size:7.1px;line-height:11.6px;color:var(--text)}
.btn{position:absolute;height:18px;padding:0 8px 0 19px;display:flex;align-items:center;font-size:7.2px;font-weight:700;color:var(--white);background:linear-gradient(#2a8fc4,#16608f);border-radius:9px 2px 2px 9px}
.btn::before{content:"";position:absolute;left:-3px;top:-2px;width:20px;height:22px;border-radius:50%;border-left:3px solid var(--accent);}

/* services */
.services{position:absolute;top:560px;left:0;width:686px;height:208px;background:var(--panel)}
.thumb{position:absolute;top:30px;width:116px;height:59px;border:2px solid #444;background:linear-gradient(135deg,#6b7c8c,#2b2f35)}
.pkg-name{position:absolute;top:97px;font-size:8.6px;font-weight:700;color:var(--ink)}
.pkg-list{position:absolute;top:111px;list-style:none;font-size:6.8px;line-height:10.2px;color:var(--text)}
.pkg-list li{display:flex;gap:4px;align-items:flex-start}
.pkg-list svg{width:7px;height:7px;margin-top:1.6px;flex:none}
.pkg-list .plus{color:var(--accent)}
.side-menu{position:absolute;left:493px;top:29px;width:117px;background:var(--side)}
.side-menu div{height:23.3px;padding-left:12px;display:flex;align-items:center;font-size:7.6px;font-weight:700;color:var(--ink);border-top:1px solid #d0d0d0}
.side-menu .head{font-family:"Exo 2",sans-serif;font-size:9px;border-top:none;height:27px}
.side-menu .on{color:var(--accent);font-weight:400}

/* testimonials */
.testi-photo{position:absolute;top:768px;left:0;width:262px;height:173px;background:linear-gradient(160deg,#bfe3f5,#6cb4d9 55%,#e8eef2)}
.testi{position:absolute;top:768px;left:262px;width:424px;height:173px;background:linear-gradient(180deg,#3ea3cf,#2f8ab5)}
.testi h2{position:absolute;left:29px;top:26px;font-size:17.5px;color:var(--white)}
.testi p{position:absolute;left:29px;top:54px;width:318px;font-size:6.9px;line-height:11px;color:#eaf6fc}
.testi .who{position:absolute;left:29px;top:132px;font-size:7.2px;font-weight:700;color:var(--white)}
.quote{position:absolute;left:252px;top:840px;width:22px;height:22px;background:#2d7fa8;transform:rotate(45deg)}
.quote-mark{position:absolute;left:254px;top:840px;width:18px;font-family:Georgia,serif;font-size:20px;color:#8fcbe7;text-align:center;line-height:26px}
.chev{position:absolute;top:840px;width:20px;height:30px}

/* inquiry */
.inq-title{position:absolute;left:76px;top:958px;font-size:16px;color:var(--ink)}
.blue{color:var(--accent)}
.inq-rule{position:absolute;left:76px;top:987px;width:315px;height:1px;background:var(--rule)}
.field{position:absolute;height:20px;border:1px solid #bbb;border-radius:2px;padding:5px 4px;font-size:6.4px;color:#777;background:var(--white)}
.submit{position:absolute;left:76px;top:1094px;width:153px;height:23px;background:linear-gradient(#2e93c6,#1a6c9a);color:var(--white);font-size:11px;font-weight:700;display:flex;align-items:center;justify-content:center;border-radius:2px;letter-spacing:.3px}

.contact{position:absolute;left:439px;top:941px;width:247px;height:201px;background:linear-gradient(160deg,#0c0c0c,#1d2226 60%,#0a0a0a)}
.contact h2{position:absolute;left:28px;top:17px;font-size:16px;color:var(--white)}
.contact .rule{position:absolute;left:28px;top:46px;width:143px;height:1px;background:#444}
.c-item{position:absolute;left:28px;display:flex;gap:8px;align-items:center;color:var(--white);font-size:6.9px;line-height:9px}
.c-icon{width:24px;height:24px;border:1px solid #aaa;border-radius:50%;display:flex;align-items:center;justify-content:center;flex:none}
.c-icon svg{width:11px;height:11px}

/* footer */
.footer{position:absolute;top:1142px;left:0;width:686px;height:58px;background:var(--black);color:var(--white)}
.foot-nav{position:absolute;left:76px;top:10px;display:flex;gap:19px;font-size:7.2px}
.foot-nav .on{color:var(--accent)}
.foot-rule{position:absolute;left:76px;top:27px;width:534px;height:1px;background:#333}
.copy{position:absolute;left:76px;top:36px;font-size:6.4px}
.socials{position:absolute;left:534px;top:6px;display:flex;gap:5px}
.socials span{width:15px;height:15px;border-radius:50%;border:1.5px solid var(--white);background:#2f5fa8}
.socials span:last-child{background:#c6303b}
.cards{position:absolute;left:523px;top:33px;display:flex;gap:2px}
.cards span{width:20px;height:12px;border-radius:1px;background:#d8d8d8}
</style>
</head>
<body>

<header class="hero">
  <div class="hero-photo" role="img" aria-label="Close-up of a glossy silver car bonnet and headlight"></div>

  <div class="brand"><span class="brand-dot"></span>glimmabay wa</div>

  <div class="info" style="left:282px">
    <svg viewBox="0 0 16 16"><circle cx="8" cy="8" r="6.5" fill="none" stroke="#2a9bd1" stroke-width="2"/><path d="M8 4v4.5h3" fill="none" stroke="#2a9bd1" stroke-width="1.6"/></svg>
    <span>Mondays – Fridays: 8am – 5pm<br>Saturdays: 8am – 1pm</span>
  </div>
  <div class="info" style="left:410px">
    <svg viewBox="0 0 16 16"><path d="M8 1a5 5 0 0 1 5 5c0 4-5 9-5 9S3 10 3 6a5 5 0 0 1 5-5z" fill="#2a9bd1"/><circle cx="8" cy="6" r="1.8" fill="#050505"/></svg>
    <span>412 Coralline Beach Road<br>Westmere Park, WA 6021</span>
  </div>
  <div class="info" style="left:526px">
    <svg viewBox="0 0 16 16"><path d="M2 6c0-2 3-3 6-3s6 1 6 3l-2 1-1-2H5L4 7zM4 8h8l1 5H3z" fill="#2a9bd1"/></svg>
    <span>For phone bookings<br><b>DAN: 0400 555 218</b></span>
  </div>

  <div class="nav-top"></div>
  <nav class="main-nav">
    <span class="on">Home</span><span>Our Packages</span><span>Our Clients</span><span>Our Gallery</span><span>Make a Booking</span><span>Find Us</span>
  </nav>

  <h1 class="hero-title">PERTH'S PREMIER<br>AUTOMOTIVE<br>DETAIL AND CAR<br>WASH CENTRE</h1>

  <div class="arrow-box" style="left:0"><svg viewBox="0 0 8 10"><path d="M6 1L2 5l4 4" fill="none" stroke="#ccc" stroke-width="1.3"/></svg></div>
  <div class="arrow-box" style="right:0"><svg viewBox="0 0 8 10"><path d="M2 1l4 4-4 4" fill="none" stroke="#ccc" stroke-width="1.3"/></svg></div>
</header>

<section>
  <h2 class="welcome-title heading">Welcome To glimmabay wa</h2>
  <div class="divider"><i></i></div>
  <p class="welcome-copy">We provide a range of service options to cater for the needs and budgets of our extensive and loyal customer base – from a simple wash through to a thorough detail, even scratch repairs. We even get the dirtiest 4WDs caked in red dust looking like new.<br>With over 20 years experience, we adopt the very latest technologies, materials and techniques to help keep your much loved vehicle as shiny and new as the day you first met. As car enthusiasts, you'll rest assured knowing that your pride and joy is taken care of, all the way, by our highly skilled technicians.</p>
  <a class="btn" style="left:310px;top:512px">Read More</a>
</section>

<section class="services">
  <div class="thumb" style="left:76px" role="img" aria-label="Hand washing a car with a sponge"></div>
  <div class="thumb" style="left:214px" role="img" aria-label="Detailing a car dashboard"></div>
  <div class="thumb" style="left:355px" role="img" aria-label="Cleaning leather car seats"></div>

  <h3 class="pkg-name" style="left:76px">MINI GLEAM</h3>
  <ul class="pkg-list" style="left:76px">
    <li><svg viewBox="0 0 8 8"><rect x=".5" y=".5" width="7" height="7" fill="none" stroke="#2a9bd1"/><path d="M1.5 4l2 2 4-5" fill="none" stroke="#2a9bd1" stroke-width="1.2"/></svg>Careful Hand Wash</li>
    <li><svg viewBox="0 0 8 8"><rect x=".5" y=".5" width="7" height="7" fill="none" stroke="#2a9bd1"/><path d="M1.5 4l2 2 4-5" fill="none" stroke="#2a9bd1" stroke-width="1.2"/></svg>Chamois Dry</li>
    <li><svg viewBox="0 0 8 8"><rect x=".5" y=".5" width="7" height="7" fill="none" stroke="#2a9bd1"/><path d="M1.5 4l2 2 4-5" fill="none" stroke="#2a9bd1" stroke-width="1.2"/></svg>Tyres Glossed</li>
  </ul>

  <h3 class="pkg-name" style="left:214px">HALF GLEAM</h3>
  <ul class="pkg-list" style="left:214px">
    <li><span><span class="plus">MINI GLEAM</span> PLUS</span></li>
    <li><svg viewBox="0 0 8 8"><rect x=".5" y=".5" width="7" height="7" fill="none" stroke="#2a9bd1"/><path d="M1.5 4l2 2 4-5" fill="none" stroke="#2a9bd1" stroke-width="1.2"/></svg>Wheels and Door Jambs Detailed</li>
    <li><svg viewBox="0 0 8 8"><rect x=".5" y=".5" width="7" height="7" fill="none" stroke="#2a9bd1"/><path d="M1.5 4l2 2 4-5" fill="none" stroke="#2a9bd1" stroke-width="1.2"/></svg>Interior Thoroughly Detailed</li>
  </ul>

  <h3 class="pkg-name" style="left:357px">FULL GLEAM</h3>
  <ul class="pkg-list" style="left:357px">
    <li><span><span class="plus">HALF GLEAM</span> PLUS</span></li>
    <li><svg viewBox="0 0 8 8"><rect x=".5" y=".5" width="7" height="7" fill="none" stroke="#2a9bd1"/><path d="M1.5 4l2 2 4-5" fill="none" stroke="#2a9bd1" stroke-width="1.2"/></svg><span>Leather Clean &amp; Condition or<br>Seats Steam Cleaned</span></li>
  </ul>

  <a class="btn" style="left:79px;top:158px">Read More</a>
  <a class="btn" style="left:216px;top:158px">Read More</a>
  <a class="btn" style="left:361px;top:158px">Read More</a>

  <div class="side-menu">
    <div class="head">All Services</div>
    <div class="on">Mini Gleam</div>
    <div>Half Gleam</div>
    <div>Full Gleam</div>
    <div>Ala Carte Add-ons</div>
    <div>Engine Testing</div>
  </div>
</section>

<section>
  <div class="testi-photo" role="img" aria-label="Two happy friends leaning out of a white car on a sunny day"></div>
  <div class="testi">
    <h2 class="heading">Client Testimonials</h2>
    <p>Lorem ipsum dolor sit amet, consectetuer adipiscing elit, sed diam nonummy nibh euismod sdf tincidunt ut laoreet dolore magna aliquam erat volutpat. Ut wisi enim ad minim veniam, quisasi nostrud exerci tation ullamcorper suscipit lobortis nisl ut aliquip ex ea commodo consequat. It' Duis autem vel eum iriure dolor in hendrerit in vulputate velit esse molestie consequat, velisae illum dolore eu feugiat nulla facilisis at vero eros et accumsan.</p>
    <div class="who">MARA TELLEN</div>
  </div>
  <div class="quote"></div>
  <div class="quote-mark">“</div>
  <svg class="chev" style="left:26px" viewBox="0 0 20 30"><path d="M16 2L4 15l12 13" fill="none" stroke="#222" stroke-width="2"/></svg>
  <svg class="chev" style="left:630px" viewBox="0 0 20 30"><path d="M4 2l12 13L4 28" fill="none" stroke="#111" stroke-width="2"/></svg>
</section>

<section>
  <h2 class="inq-title heading">Quick <span class="blue">Inquiry</span></h2>
  <div class="inq-rule"></div>
  <div class="field" style="left:76px;top:998px;width:153px">Fast Names*</div>
  <div class="field" style="left:237px;top:998px;width:154px">Last Names*</div>
  <div class="field" style="left:76px;top:1027px;width:153px">Email *</div>
  <div class="field" style="left:237px;top:1027px;width:154px">Phone*</div>
  <div class="field" style="left:76px;top:1053px;width:315px;height:30px">Message *</div>
  <div class="submit">SUBMIT</div>

  <div class="contact">
    <h2 class="heading">Contact <span class="blue">Details</span></h2>
    <div class="rule"></div>
    <div class="c-item" style="top:65px">
      <div class="c-icon"><svg viewBox="0 0 16 16"><path d="M8 1a5 5 0 0 1 5 5c0 4-5 9-5 9S3 10 3 6a5 5 0 0 1 5-5z" fill="#2a9bd1"/><circle cx="8" cy="6" r="1.8" fill="#111"/></svg></div>
      <span>glimmabay wa<br>412 Coralline Beach Road<br>Westmere Park WA 6021</span>
    </div>
    <div class="c-item" style="top:116px">
      <div class="c-icon"><svg viewBox="0 0 16 16"><path d="M4 1h3l1 4-2 1a8 8 0 0 0 4 4l1-2 4 1v3l-2 2C7 14 2 9 2 3z" fill="#2a9bd1"/></svg></div>
      <span>Phone:<br>08 5550 1472</span>
    </div>
    <div class="c-item" style="top:164px">
      <div class="c-icon"><svg viewBox="0 0 16 16"><rect x="1" y="3" width="14" height="10" rx="1" fill="#2a9bd1"/><path d="M1.5 4l6.5 5 6.5-5" fill="none" stroke="#111" stroke-width="1.2"/></svg></div>
      <span>Email:<br>info@glimmabaywa.com.</span>
    </div>
  </div>
</section>

<footer class="footer">
  <nav class="foot-nav">
    <span class="on">Home</span><span>Our Packages</span><span>Our Clients</span><span>Our Gallery</span><span>Make a Booking</span><span>Find Us</span>
  </nav>
  <div class="socials" aria-label="Social links"><span></span><span></span><span></span><span></span></div>
  <div class="foot-rule"></div>
  <div class="copy">Copyright © 2016 glimmabay wa | All Rights Reserved</div>
  <div class="cards" aria-label="Accepted payment methods"><span></span><span></span><span></span><span></span></div>
</footer>

</body>
</html>
```